Double Sided Flyer for 3D printing services company

We need a nice balanced flyer for our corporate handout. The attached is for concept only and not the final design. We think the attached examples have elements that balance nicely but the graphics are not good. We are attaching the logo from the corporate office for our new logo. We will add the company information after the final design is selected for web address, phone, mailing etc. Please leave room for that information in the design. Please ask any questions prior to submission. Our main focus is printing RUBBER 3D Parts and not plastic parts. The images selected should be focused on that. We also need to ensure the images are approved for use in a corporate flyer for content.

```html
<!DOCTYPE html>
<html lang="en">
<head>
<meta charset="utf-8">
<title>Kestrel 3D Printing Flyer</title>
<link href="https://fonts.googleapis.com/css2?family=Montserrat:ital,wght@0,300;0,400;0,700;0,800;1,700;1,800&family=Lato:ital,wght@0,400;0,700;1,400;1,700&display=swap" rel="stylesheet">
<style>
:root{
  --stage:#b3b3b3;
  --ink:#0c1017;
  --orange:#f06a1e;
  --orange-deep:#e2531f;
  --red:#e0321d;
  --green:#6b9a4a;
  --steel:#6f8fae;
  --grey-text:#a9adb3;
  --white:#ffffff;
}
*{margin:0;padding:0;box-sizing:border-box}
html,body{width:1200px;height:814px;overflow:hidden;background:var(--stage)}
body{position:relative;font-family:'Lato',sans-serif;color:var(--white)}
.flyer{position:absolute;left:51px;top:52px;width:1098px;height:710px;background:var(--ink);overflow:hidden}
.page{position:absolute;top:0;height:710px}
.page--front{left:0;width:548px;overflow:hidden}
.page--back{left:548px;width:550px}
.abs{position:absolute}
.art{position:absolute;left:0;top:0}
.brand{display:flex;align-items:center;gap:6px}
.brand__dot{width:22px;height:22px;border-radius:50%;background:var(--orange)}
.brand__name{font-family:'Montserrat',sans-serif;font-weight:800;font-size:22px;letter-spacing:1px;color:var(--white);line-height:1}
.brand__tag{font-family:'Lato',sans-serif;font-size:7px;letter-spacing:1.4px;color:var(--grey-text);margin-left:28px;margin-top:2px}
.hero-3d{left:50px;top:290px;font-family:'Montserrat',sans-serif;font-weight:800;font-size:170px;line-height:1;letter-spacing:-10px;
  background:linear-gradient(180deg,#ff6a4a 0%,var(--red) 45%,#9d1a10 100%);-webkit-background-clip:text;background-clip:text;color:transparent}
.hero-line{left:53px;font-family:'Montserrat',sans-serif;font-size:41px;line-height:1;color:var(--orange)}
.hero-line--bold{font-weight:700;letter-spacing:.5px}
.hero-line--light{font-weight:300;font-size:44px}
.subhead{left:53px;top:600px;font-family:'Lato',sans-serif;font-style:italic;font-weight:700;font-size:18px;line-height:22px;color:var(--steel)}
.why__title{left:323px;top:478px;font-family:'Montserrat',sans-serif;font-weight:800;font-style:italic;font-size:25px;color:var(--ink);letter-spacing:-.5px}
.why__item{font-family:'Lato',sans-serif;font-style:italic;font-size:16.5px;color:var(--ink);line-height:19px}
.why__icon{position:absolute}
.quick{left:33px;top:32px;font-family:'Montserrat',sans-serif;font-weight:800;font-style:italic;font-size:26px;line-height:31px;color:var(--green)}
.redefine{left:33px;top:104px;font-family:'Montserrat',sans-serif;font-weight:300;font-size:26px;line-height:30px;color:var(--orange);letter-spacing:.5px}
.redefine b{font-weight:700}
.gasket{left:33px;top:202px;font-family:'Montserrat',sans-serif;font-weight:300;font-size:23px;line-height:27px;color:var(--grey-text);letter-spacing:.5px}
.lead{left:33px;top:264px;width:190px;font-size:13px;line-height:15px;font-weight:700}
.easy{left:33px;top:322px;font-style:italic;font-weight:700;font-size:15px}
.steps{left:33px;top:356px;font-size:10.5px;line-height:14.5px;list-style:none}
.confirm{left:33px;top:412px;width:220px;font-size:13px;line-height:15px;font-weight:700}
.quote__mark{left:37px;top:458px;width:36px;height:36px;border-radius:50%;background:var(--steel);color:var(--white);font-family:'Montserrat',sans-serif;font-weight:800;font-size:24px;text-align:center;line-height:40px}
.quote__text{left:77px;top:466px;width:182px;font-size:10.8px;line-height:14.3px}
.quote__by{left:77px;top:596px;font-size:11px}
.code-box{left:30px;top:622px;width:62px;height:62px;background:var(--white)}
.contact{left:320px;top:638px;font-size:12px;line-height:19px;color:var(--grey-text)}
.contact li{list-style:none;display:flex;align-items:center;gap:16px}
.contact svg{flex:none}
.benefits__title{left:289px;top:210px;font-family:'Montserrat',sans-serif;font-weight:300;font-size:26px;line-height:30px;color:var(--orange);letter-spacing:.5px}
.benefits__title b{font-weight:700}
.benefit{left:345px;width:182px}
.benefit h3{font-family:'Lato',sans-serif;font-weight:700;font-size:10.8px;line-height:13px;text-transform:uppercase}
.benefit p{font-size:9.3px;line-height:11.8px;color:var(--grey-text)}
</style>
</head>
<body>
<main class="flyer">

  <!-- FRONT -->
  <section class="page page--front">
    <svg class="art" width="548" height="710" viewBox="0 0 548 710">
      <defs>
        <radialGradient id="machineTone" cx="50%" cy="45%" r="60%">
          <stop offset="0" stop-color="#c6d2dd"/>
          <stop offset=".55" stop-color="#6f88a1"/>
          <stop offset="1" stop-color="#1d2a38"/>
        </radialGradient>
        <linearGradient id="discTone" x1="0" y1="0" x2="1" y2="1">
          <stop offset="0" stop-color="#e8471f"/>
          <stop offset="1" stop-color="#e07a22"/>
        </linearGradient>
      </defs>
      <ellipse role="img" aria-label="Photo: 3D printer nozzle printing a rubber lattice part" cx="290" cy="250" rx="260" ry="222" fill="url(#machineTone)"/>
      <path d="M40 420 C-10 250 90 60 300 35 C420 20 520 80 540 150" fill="none" stroke="#6c6f74" stroke-width="12" stroke-linecap="round"/>
      <path d="M60 300 C40 160 150 40 320 45 C440 50 510 140 500 230" fill="none" stroke="var(--orange)" stroke-width="14" stroke-linecap="round"/>
      <path d="M500 150 C560 300 470 420 330 440" fill="none" stroke="var(--orange-deep)" stroke-width="10" stroke-linecap="round"/>
      <path d="M470 160 C540 260 500 360 420 400" fill="none" stroke="#6c6f74" stroke-width="7" stroke-linecap="round"/>
      <circle cx="575" cy="775" r="370" fill="url(#discTone)"/>
    </svg>

    <div class="abs brand" style="left:372px;top:42px;flex-direction:column;align-items:flex-start;gap:0">
      <div class="brand"><span class="brand__dot"></span><span class="brand__name">KESTREL</span></div>
      <span class="brand__tag">SEALS·GASKETS·HOSES</span>
    </div>

    <div class="abs hero-3d">3D</div>
    <div class="abs hero-line hero-line--bold" style="top:461px">PRINTING</div>
    <div class="abs hero-line hero-line--light" style="top:507px">MADE</div>
    <div class="abs hero-line hero-line--light" style="top:554px">EASY</div>
    <div class="abs subhead">POLYJET<br>PRINTING OF<br>RUBBER AND<br>ELECTRONIC PARTS</div>

    <div class="abs why__title">WHY WE ARE...</div>

    <svg class="why__icon" style="left:284px;top:518px" width="26" height="30" viewBox="0 0 26 30" fill="var(--ink)">
      <path d="M3 2h16v3l-6 7 6 7v3H3v-3l6-7-6-7z"/><circle cx="20" cy="24" r="5"/>
    </svg>
    <div class="abs why__item" style="left:326px;top:518px">Reduce Time to Market from<br>Weeks to Hours</div>

    <svg class="why__icon" style="left:266px;top:564px" width="30" height="28" viewBox="0 0 30 28" fill="var(--ink)">
      <rect x="1" y="7" width="22" height="15" rx="3"/><circle cx="24" cy="6" r="5"/>
      <circle cx="6" cy="14" r="1.6" fill="var(--orange)"/><circle cx="12" cy="14" r="1.6" fill="var(--orange)"/><circle cx="18" cy="14" r="1.6" fill="var(--orange)"/>
    </svg>
    <div class="abs why__item" style="left:312px;top:573px">Eliminate Costly Design Errors</div>

    <svg class="why__icon" style="left:266px;top:606px" width="32" height="30" viewBox="0 0 32 30">
      <circle cx="19" cy="16" r="10" fill="none" stroke="var(--ink)" stroke-width="3"/>
      <path d="M19 16V9M19 16h5" stroke="var(--ink)" stroke-width="2.5"/>
      <path d="M2 13h7M0 17h8M2 21h7" stroke="var(--ink)" stroke-width="2"/>
      <rect x="16" y="2" width="6" height="3" fill="var(--ink)"/>
    </svg>
    <div class="abs why__item" style="left:312px;top:614px">Faster Time to Market</div>

    <svg class="why__icon" style="left:282px;top:650px" width="32" height="30" viewBox="0 0 32 30" fill="var(--ink)">
      <circle cx="10" cy="10" r="8"/><circle cx="22" cy="20" r="8"/>
      <circle cx="10" cy="10" r="3" fill="var(--orange)"/><circle cx="22" cy="20" r="3" fill="var(--orange)"/>
    </svg>
    <div class="abs why__item" style="left:330px;top:659px">Faster Time to Market</div>
  </section>

  <!-- BACK -->
  <section class="page page--back">
    <svg class="art" width="550" height="710" viewBox="0 0 550 710">
      <defs>
        <linearGradient id="partsTone" x1="0" y1="0" x2="1" y2="1">
          <stop offset="0" stop-color="#e4e5e7"/>
          <stop offset=".5" stop-color="#8d9094"/>
          <stop offset=".8" stop-color="#3a3c40"/>
          <stop offset="1" stop-color="#c9373c"/>
        </linearGradient>
      </defs>
      <path role="img" aria-label="Photo: assorted black and red rubber seals, gaskets, grommets and O-rings"
        d="M230 0H550V276C520 285 490 270 470 240C445 205 405 225 380 205C350 180 330 175 300 180C265 186 260 150 270 125C282 95 265 70 275 45C285 20 250 10 230 0Z"
        fill="url(#partsTone)"/>
      <line x1="309" y1="298" x2="309" y2="593" stroke="var(--white)" stroke-width="2"/>
      <g stroke="var(--white)" stroke-width="2.5" fill="var(--orange)">
        <circle cx="309" cy="298" r="20"/><circle cx="309" cy="372" r="20"/>
        <circle cx="309" cy="446" r="20"/><circle cx="309" cy="519" r="20"/>
        <circle cx="309" cy="593" r="20"/>
      </g>
      <g fill="none" stroke="var(--white)" stroke-width="2">
        <path d="M299 304a10 10 0 1 1 20 0"/><path d="M309 304l5-6"/>
        <path d="M303 366h12v10l-6 5-6-5z"/><text x="306" y="376" fill="var(--white)" stroke="none" font-size="9" font-family="Lato">$</text>
        <path d="M297 446l6-6 6 4 6-4 6 6-8 7h-8z"/>
        <circle cx="309" cy="515" r="6"/><path d="M306 523h6M307 526h4"/>
        <circle cx="305" cy="596" r="5"/><circle cx="314" cy="588" r="4"/>
      </g>
    </svg>

    <div class="abs quick">QUICK<br>PROTOTYPING</div>
    <div class="abs redefine">REDEFINE YOUR<br>INDUSTRY WITH<br><b>3D PRINTING</b></div>
    <div class="abs gasket">GASKET AND<br>RUBBER PARTS</div>
    <p class="abs lead">Need quality? Let us print your custom one-off or production pieces.</p>
    <p class="abs easy">EASY AS 1*2*3</p>
    <ol class="abs steps">
      <li>1. Send us your rubber part design file</li>
      <li>2. Receive your Estimate within 24 hours</li>
      <li>3. Receive your Prototype sample within 10 days</li>
    </ol>
    <p class="abs confirm">Confirm fitment and function before losing time and money on costly mold</p>

    <div class="abs quote__mark">“</div>
    <p class="abs quote__text">Lorem Ipsum is simply dummy text of the printing and typesetting industry. Lorem Ipsum has been the industry's standard unknown specimen book. It has survived not only five centuries, but also the leap into electronic typesetting, remaining essentially unchanged.</p>
    <p class="abs quote__by">-Mara Quill</p>

    <div class="abs code-box"></div>

    <div class="abs" style="left:122px;top:646px">
      <div class="brand"><span class="brand__dot"></span><span class="brand__name" style="font-size:24px">KESTREL</span></div>
      <div class="brand__tag">SEALS·GASKETS·HOSES</div>
    </div>

    <ul class="abs contact">
      <li><svg width="14" height="14" viewBox="0 0 14 14"><path d="M3 1l3 3-2 2c1 2 2 3 4 4l2-2 3 3-2 2C6 13 1 8 1 3z" fill="var(--orange)"/></svg>555-013-4470</li>
      <li><svg width="14" height="14" viewBox="0 0 14 14"><rect x="1" y="3" width="12" height="8" fill="var(--orange)"/><path d="M1 3l6 5 6-5" stroke="var(--ink)" fill="none"/></svg>info@kestrelparts.com</li>
      <li><svg width="14" height="14" viewBox="0 0 14 14" fill="none" stroke="var(--orange)" stroke-width="1.5"><circle cx="7" cy="7" r="6"/><ellipse cx="7" cy="7" rx="2.5" ry="6"/><path d="M1 7h12"/></svg>kestrelparts.com</li>
    </ul>

    <div class="abs benefits__title">BENEFITS OF<br><b>3D PRINTING</b></div>

    <div class="abs benefit" style="top:281px"><h3>Speed Time to Market</h3><p>Compress design cycles by 3D printing multiple prototypes on demand, right in your office.</p></div>
    <div class="abs benefit" style="top:352px"><h3>Reduce Development Cost</h3><p>Cut traditional prototyping and tooling cost. Identify design errors earlier and reduce travel to production facilities.</p></div>
    <div class="abs benefit" style="top:431px"><h3>Win Business</h3><p>Bring realistic 3D models to prospective accounts, sponsors and focus groups.</p></div>
    <div class="abs benefit" style="top:499px"><h3>Increase Innovation</h3><p>Print prototypes in hours, obtain feedback, refine designs and repeat the cycle until designs are perfect.</p></div>
    <div class="abs benefit" style="top:573px"><h3>Personalise Products</h3><p>Personalise merchandise such as pens and other items at conventions etc. This can increase mindshare with potential clients.</p></div>
  </section>
</main>
</body>
</html>
```